Clean, Fresh Business Card Design Needed

We need a business card design for a new business we have taken over called "Bonders and Fillers". We got a logo through this website which i have attached. We are wanting something that is vibrant but clean and fresh. Our business mainly sells glue. Maybe a cool design/slogan on the back? Modern, sleek.

Industry/Entity Type

Business

Contact Information for Business Card

Name: Ewan Tressider, Managing Director. Address: 164 Kelmond Road, Tauranga 3117, Phone: 07 462 3947 Mobile: 021 354 921 Fax: 07 462 5086 Email: bondfill.mail@pelorix.co.nz, Web: www.stickwarex.co.nz

Font styles to use
Serif

Requirements
Must have
• All business card details, logo.
Nice to have
• Design, slogan on back of card

```html
<!DOCTYPE html>
<html lang="en">
<head>
<meta charset="utf-8">
<title>Bonders and Fillers – Business Card</title>
<link rel="stylesheet" href="https://fonts.googleapis.com/css2?family=Marcellus&family=Arimo:wght@400;700&display=swap">
<style>
  :root {
    --stage: #e9e7e3;
    --card: #ffffff;
    --brand-blue: #2f3ea8;
    --blue-light: #5566c4;
    --ink: #1f1f24;
    --swoosh: #2e2f33;
    --title: #5a64b8;
    --on-blue: #ffffff;
  }
  * { margin: 0; padding: 0; box-sizing: border-box; }
  html, body { width: 1200px; height: 858px; overflow: hidden; background: var(--stage); }
  .canvas { position: relative; width: 1200px; height: 858px; }

  .card {
    position: absolute;
    width: 640px; height: 356px;
    background: var(--card);
    box-shadow: 0 6px 18px rgba(0,0,0,.18);
    overflow: hidden;
  }
  .card--front { left: 280px; top: 50px; }
  .card--back  { left: 280px; top: 452px; }

  .front-waves { position: absolute; inset: 0; width: 100%; height: 100%; }

  .brand { position: absolute; display: flex; align-items: center; gap: 14px; }
  .brand__square { width: 58px; height: 58px; background: var(--brand-blue); border-radius: 8px; flex: none; }
  .brand__name {
    font-family: "Marcellus", serif;
    color: var(--ink);
    font-size: 28px;
    line-height: 1.05;
    letter-spacing: 3px;
    text-transform: uppercase;
    white-space: nowrap;
  }
  .card--front .brand { left: 34px; top: 42px; }

  .person { position: absolute; left: 40px; bottom: 70px; font-family: "Arimo", sans-serif; }
  .person__name { font-size: 24px; font-weight: 700; color: var(--ink); }
  .person__role { font-size: 17px; color: var(--title); margin-top: 2px; }

  .contacts {
    position: absolute; right: 24px; top: 56px;
    list-style: none;
    font-family: "Arimo", sans-serif;
    color: var(--on-blue);
    font-size: 14px;
    text-align: right;
  }
  .contacts li { display: flex; justify-content: flex-end; align-items: center; gap: 10px; height: 27px; white-space: nowrap; }
  .contacts svg { width: 15px; height: 15px; flex: none; fill: var(--on-blue); }

  .card--back .brand { left: 50%; top: 50%; transform: translate(-50%, -50%); gap: 20px; }
  .card--back .brand__square { width: 78px; height: 78px; border-radius: 10px; }
  .card--back .brand__name { font-size: 36px; }
</style>
</head>
<body>
<main class="canvas">

  <section class="card card--front" aria-label="Business card front">
    <svg class="front-waves" viewBox="0 0 640 356" aria-hidden="true">
      <path d="M400 0 C300 70 330 250 250 356 L640 356 L640 0 Z" fill="var(--brand-blue)"/>
      <path d="M385 0 C290 80 315 240 232 356 L250 356 C330 250 300 70 400 0 Z" fill="var(--blue-light)"/>
      <path d="M415 0 C320 80 345 240 290 356 L300 356 C358 240 335 80 430 0 Z" fill="#ffffff" opacity=".85"/>
      <path d="M175 356 C270 330 305 260 300 170 C318 270 290 335 228 356 Z" fill="var(--swoosh)"/>
    </svg>

    <div class="brand">
      <span class="brand__square"></span>
      <span class="brand__name">Bonders<br>and Fillers</span>
    </div>

    <div class="person">
      <p class="person__name">Ewan Tressider</p>
      <p class="person__role">Managing Director</p>
    </div>

    <ul class="contacts">
      <li>07 462 3947<svg viewBox="0 0 16 16"><path d="M3 1h3l1 4-2 1c1 2 3 4 5 5l1-2 4 1v3c0 1-1 2-2 2C7 15 1 9 1 3c0-1 1-2 2-2z"/></svg></li>
      <li>021 354 921<svg viewBox="0 0 16 16"><path d="M4 0h8v16H4zM5.5 2v10h5V2z"/></svg></li>
      <li>07 462 5086<svg viewBox="0 0 16 16"><path d="M4 1h8v4H4zM1 6h14v7h-3v2H4v-2H1zM5 11v3h6v-3z"/></svg></li>
      <li>bondfill.mail@pelorix.co.nz<svg viewBox="0 0 16 16"><path d="M1 3h14v10H1zM2 4l6 5 6-5v-.5H2z"/></svg></li>
      <li>www.stickwarex.co.nz<svg viewBox="0 0 16 16"><circle cx="8" cy="8" r="7"/><path d="M1 8h14M8 1c-3 4-3 10 0 14M8 1c3 4 3 10 0 14" stroke="var(--brand-blue)" stroke-width="1" fill="none"/></svg></li>
      <li>164 Kelmond Road, Tauranga 3117<svg viewBox="0 0 16 16"><path d="M8 1l7 7h-2v7H9v-4H7v4H3V8H1z"/></svg></li>
    </ul>
  </section>

  <section class="card card--back" aria-label="Business card back">
    <div class="brand">
      <span class="brand__square"></span>
      <span class="brand__name">Bonders<br>and Fillers</span>
    </div>
  </section>

</main>
</body>
</html>
```